Junior Builders Coastline Gala Poster

To Create a Poster for the Junior Builders Coastline Gala 2013

Target Market(s)

Young Professional Engineers aged 18-35. Male and Female

Requirements
Must have
• All Details required for the ball. Black and white/silver theme. Some kind of engineering theme. Must have the following text:

Join us in celebrating the Annual Junior Builders of Coastline Region Gala with a night of dinner and entertainment.
Saturday July 13th, 2013
Time: 7pm Arrival
Venue: Corvane Lodge Hotel, Perth
Dress: Formal
The evening will include drinks, a three-course dinner, music and dancing.
Ticket price $139, on sale now! To purchase tickets go to:
(website to be announced)
Proceeds go to Makers Across Rivers
is is an 18+ event. Open to general public.
Nice to have
• Modern, Classy, Similar to previous years designs. Possibly Masquerade themed.
Should not have
• Fish, environmental theme, rural Australia theme (these have been done)

```html
<!DOCTYPE html>
<html lang="en">
<head>
<meta charset="utf-8">
<title>Junior Builders Coastline Gala</title>
<link href="https://fonts.googleapis.com/css2?family=Great+Vibes&family=Didact+Gothic&display=swap" rel="stylesheet">
<style>
  :root {
    --bg: #1d1d1d;
    --ink: #eeeeee;
    --ink-soft: #d6d6d6;
    --rule: #8a8a8a;
    --band: #4a4a4a;
    --band-dark: #2c2c2c;
    --footer: #ffffff;
    --partner-ink: #1b2a3a;
    --support-green: #5fa832;
    --support-grey: #8e9a86;
  }
  * { margin: 0; padding: 0; box-sizing: border-box; }
  html, body { width: 1200px; height: 2414px; overflow: hidden; background: var(--bg); }
  .poster {
    position: relative; width: 1200px; height: 2414px; background: var(--bg);
    font-family: "Didact Gothic", "Helvetica Neue", Arial, sans-serif; color: var(--ink);
  }
  .hero-mask {
    position: absolute; left: 0; top: 0; width: 1200px; height: 820px;
    background:
      radial-gradient(ellipse 340px 170px at 600px 400px, #b59a5e 0%, #7a6640 35%, rgba(60,52,40,0.5) 65%, rgba(29,29,29,0) 100%),
      radial-gradient(ellipse 620px 420px at 600px 330px, #8c8c8c 0%, #4a4a4a 45%, #1d1d1d 90%);
  }
  .centered { position: absolute; left: 0; width: 1200px; text-align: center; }
  .kicker { top: 850px; font-size: 28px; letter-spacing: 4px; }
  .title {
    font-family: "Great Vibes", cursive; font-weight: 400; font-size: 92px; line-height: 120px;
    top: 925px; color: #ffffff;
  }
  .subline { top: 1178px; font-size: 28px; letter-spacing: 3.5px; }
  .host-name {
    top: 1345px; display: flex; justify-content: center; align-items: center; gap: 22px;
    font-size: 34px; letter-spacing: 2px; color: var(--ink);
  }
  .host-name .mark { width: 60px; height: 60px; background: #e23a2c; }
  .rule { position: absolute; left: 290px; width: 652px; height: 2px; background: var(--rule); }
  .rule.top { top: 1536px; }
  .rule.bottom { top: 1802px; }
  .date { top: 1578px; font-size: 32px; letter-spacing: 3px; }
  .detail { font-size: 31px; letter-spacing: 2px; }
  .detail span { font-size: 26px; letter-spacing: 1.5px; }
  .d-time { top: 1636px; }
  .d-venue { top: 1680px; }
  .d-dress { top: 1724px; }
  .info { position: absolute; left: 97px; width: 1020px; font-size: 22px; letter-spacing: 1.8px; line-height: 41px; color: var(--ink-soft); }
  .info.drinks { top: 1880px; }
  .info.tickets { top: 1948px; }
  .info.cause { top: 2049px; }
  .band { position: absolute; left: 0; top: 2173px; width: 1200px; height: 44px; background: linear-gradient(#5b5b5b, var(--band-dark)); }
  .band-label { position: absolute; top: 8px; font-size: 22px; letter-spacing: 2px; color: #ffffff; }
  .band-label.partner { left: 140px; }
  .band-label.support { left: 665px; }
  .band .tab { position: absolute; left: 0; top: 0; width: 350px; height: 44px; background: var(--band); clip-path: polygon(0 0, 330px 0, 350px 44px, 0 44px); }
  .footer { position: absolute; left: 0; top: 2217px; width: 1200px; height: 197px; background: var(--footer); }
  .sponsor { position: absolute; font-family: "Didact Gothic", Arial, sans-serif; }
  .sponsor.partner { left: 109px; top: 62px; font-size: 64px; letter-spacing: 2px; color: var(--partner-ink); }
  .sponsor.relief { left: 463px; top: 50px; width: 177px; height: 96px; background: var(--support-green); color: #ffffff; font-size: 34px; display: flex; align-items: center; justify-content: center; }
  .badge { position: absolute; left: 690px; top: 48px; width: 160px; height: 100px; background: #c9d67a; }
  .sponsor.rivers { left: 893px; top: 62px; width: 230px; font-size: 28px; line-height: 34px; color: var(--support-grey); }
</style>
</head>
<body>
<div class="poster">
  <div class="hero-mask" role="img" aria-label="Ornate gold masquerade mask framed by dark grey feathers"></div>

  <p class="centered kicker">JOIN US IN CELEBRATING</p>
  <h1 class="centered title">The Annual Junior Builders<br>of Coastline Region Gala</h1>
  <p class="centered subline">WITH A NIGHT OF DINNER AND ENTERTAINMENT</p>

  <div class="centered host-name"><span class="mark"></span><span>Structura Guild Junior Builders</span></div>

  <div class="rule top"></div>
  <p class="centered date">SATURDAY JULY 13TH, 2013</p>
  <p class="centered detail d-time">TIME: <span>7pm Arrival</span></p>
  <p class="centered detail d-venue">VENUE: <span>Corvane Lodge Hotel, Perth</span></p>
  <p class="centered detail d-dress">DRESS: <span>Formal</span></p>
  <div class="rule bottom"></div>

  <p class="info drinks">The evening will include drinks, a three-course dinner, music and dancing.</p>
  <p class="info tickets">Ticket price $139, on sale now! To purchase tickets go to:<br>https://events.structuraguild.org.au</p>
  <p class="info cause">Proceeds go to Makers Across Rivers<br>Is an 18+ event. Open to general public.</p>

  <div class="band">
    <div class="tab"></div>
    <span class="band-label partner">EVENT PARTNER</span>
    <span class="band-label support">IN SUPPORT OF</span>
  </div>

  <div class="footer">
    <span class="sponsor partner">Veltrane</span>
    <span class="sponsor relief">Helpwell</span>
    <div class="badge"></div>
    <span class="sponsor rivers">Makers Across Rivers</span>
  </div>
</div>
</body>
</html>
```